Slide Master for Harrowfield Engines - A Systematic Hedge Fund

We are looking for someone to produce a theme and slide master for us for our investor presentations. I have uploaded a few examples of templates that we would like to have included:
Main Title
Section Title
Slides with just bullet points
Different image/table configurations with bullet points and foot notes
Biographies of different lengths
A disclaimer (no one will read this but it should still look nice and needs to be in the presentations)
I have also uploaded the company logo, business card and colour definitions. Currently we have a blue colour scheme defined, but it would be nice to get a complementary set of colours so that when we have charts with more elements we can just draw from those.
The most important thing is that the slide master must be of general use to us. We arn't looking to have a specific presentation designed for us, but a theme/style that we can apply ourselves to any presentation we need to give in the future. It should have clearly defined guidelines for where content should go (and if this is different with and without footnotes for example). We would also like it to have a similar feel to the logo/business cards, so matt colours, high contrast, but not busy.
I'm excited to see the results!

```html
<!DOCTYPE html>
<html lang="en">
<head>
<meta charset="utf-8">
<title>Harrowfield Engines – Slide Master Overview</title>
<link href="https://fonts.googleapis.com/css2?family=Roboto:ital,wght@0,300;0,400;0,500;0,700;1,400&family=PT+Sans&display=swap" rel="stylesheet">
<style>
  :root{
    --navy:#16385f;
    --ink:#3d3d3d;
    --ink-soft:#666;
    --purple:#8272c4;
    --purple-pale:#d9d4ee;
    --magenta:#cf8fb0;
    --rule:#ead7e0;
    --frame:#cfcfcf;
    --band:#e9e9e9;
    --note:#6dbb3c;
    --bar-light:#d6d6d6;
    --bar-dark:#5a5a5a;
  }
  html,body{margin:0;padding:0;width:720px;height:1200px;overflow:hidden;background:#fff;}
  .canvas{position:relative;width:720px;height:1200px;overflow:hidden;background:#fff;}
  .sheet{position:absolute;left:0;top:0;width:1476px;height:2460px;transform:scale(.4878);transform-origin:0 0;font-family:"Roboto",sans-serif;color:var(--ink);}

  .guides{position:absolute;left:0;top:0;width:1476px;height:2460px;}
  .note{position:absolute;font-family:"PT Sans",sans-serif;color:var(--note);font-size:11px;line-height:1.15;white-space:nowrap;}
  .note--label{font-size:12px;}
  .note--text{white-space:normal;}
  .note p{margin:0 0 12px;}

  .slide{position:absolute;width:634px;height:355px;border:1px solid var(--frame);background:#fff;box-sizing:border-box;overflow:hidden;}
  .slide__rule{position:absolute;left:95px;right:0;top:44px;height:1px;background:var(--rule);}
  .slide__dot{position:absolute;width:5px;height:5px;border-radius:50%;background:var(--rule);top:42px;}
  .slide__title{position:absolute;left:57px;top:21px;font-size:16px;font-weight:300;color:var(--ink);white-space:nowrap;}
  .slide__subtitle{position:absolute;left:95px;top:47px;font-size:11.5px;font-weight:700;color:#222;white-space:nowrap;}
  .slide__brand{position:absolute;left:56px;top:298px;font-size:11px;font-weight:700;color:var(--navy);white-space:nowrap;display:flex;align-items:center;gap:4px;}
  .slide__brand::before{content:"";width:6px;height:6px;background:var(--navy);}
  .slide__stamp{position:absolute;right:12px;bottom:6px;font-size:5.5px;color:#444;letter-spacing:.1px;}

  .block{position:absolute;font-size:9px;line-height:13.4px;color:var(--ink);}
  .block__head{font-size:11.5px;font-weight:700;color:var(--purple);margin:0 0 6px;}
  .block ol{margin:0;padding-left:16px;}
  .block p{margin:0 0 10px;}

  .slide--cover .cover__title{position:absolute;left:357px;top:76px;font-size:24px;font-weight:300;line-height:30px;color:var(--ink);}
  .slide--cover .cover__brand{position:absolute;left:100px;top:222px;font-size:25px;font-weight:700;color:var(--navy);display:flex;align-items:center;gap:8px;}
  .slide--cover .cover__brand::before{content:"";width:12px;height:12px;border-radius:50%;background:var(--navy);}

  .slide--section .section__title{position:absolute;left:55px;top:157px;font-size:20px;font-weight:300;color:var(--ink);white-space:nowrap;}

  .chart{position:absolute;box-sizing:border-box;background:#fff;}
  .chart--purple{border:2px solid var(--purple-pale);}
  .chart--magenta{border:2px solid #e2bcd0;}
  .chart--line{border:2px solid #a99ad8;}
  .chart svg{display:block;width:100%;height:100%;}

  .footnotes{position:absolute;left:271px;top:323px;font-size:5.5px;line-height:7px;color:#444;width:260px;}

  .datatable{position:absolute;left:259px;top:95px;width:350px;border-collapse:separate;border-spacing:3px;border:1px solid var(--purple-pale);font-size:6px;}
  .datatable th{background:var(--purple-pale);font-weight:700;color:#333;line-height:7px;height:16px;padding:1px;text-align:center;}
  .datatable td{height:18px;border-bottom:2px solid var(--purple-pale);border-right:2px solid var(--purple-pale);}

  .banded{position:absolute;left:83px;top:116px;width:464px;font-size:9px;color:var(--ink);}
  .banded .block__head{margin-left:17px;}
  .banded ol{margin:0;padding:0;list-style:none;}
  .banded li{padding:2px 17px;line-height:13.4px;display:flex;gap:7px;}
  .banded li:nth-child(odd){background:var(--band);}

  .legal{position:absolute;top:65px;width:280px;font-size:6.2px;line-height:9.6px;color:#444;}
  .legal p{margin:0 0 9px;}

  .bio{position:absolute;top:66px;width:222px;height:194px;border:2px solid #e3def3;border-radius:14px;box-sizing:border-box;padding:8px 15px;font-size:8.6px;line-height:12px;color:var(--ink);}
  .bio h3{margin:0 0 6px;font-size:11.5px;font-weight:700;color:var(--purple);}
  .bio p{margin:0;}
</style>
</head>
<body>
<div class="canvas">
<div class="sheet">

  <svg class="guides" viewBox="0 0 1476 2460" aria-hidden="true">
    <defs>
      <marker id="tip" viewBox="0 0 6 6" refX="5" refY="3" markerWidth="5" markerHeight="5" orient="auto"><path d="M0 0L6 3L0 6Z" fill="#6dbb3c"/></marker>
    </defs>
    <g stroke="#6dbb3c" stroke-width="1" fill="none">
      <line x1="946" y1="199" x2="855" y2="199" marker-end="url(#tip)"/>
      <line x1="512" y1="567" x2="616" y2="567" marker-end="url(#tip)"/>
      <line x1="143" y1="757" x2="247" y2="757" marker-end="url(#tip)"/>
      <line x1="219" y1="1218" x2="357" y2="1218" marker-end="url(#tip)"/>
      <line x1="330" y1="1197" x2="383" y2="1155" marker-end="url(#tip)"/>
      <line x1="233" y1="1537" x2="285" y2="1580" marker-end="url(#tip)"/>
    </g>
  </svg>

  <div class="note note--label" style="left:876px;top:186px;">Title screen</div>
  <div class="note note--label" style="left:512px;top:554px;">Section title screen</div>
  <div class="note note--label" style="left:143px;top:744px;">Section title screen</div>
  <div class="note note--label" style="left:219px;top:1205px;">Graphs and table screens</div>
  <div class="note note--label" style="left:175px;top:1550px;">Text screen</div>
  <div class="note note--text" style="left:84px;top:532px;width:280px;">
    <p>Logo elements, lines and dots, are expanded to create a backdrop for these slides.</p>
    <p>Two new colours, lighter shades of purple and magenta, are introduced as accent colours in the presentation.</p>
    <p>Developed in Deckwright.</p>
  </div>

  <!-- Title screen -->
  <section class="slide slide--cover" style="left:211px;top:64px;">
    <div class="slide__rule"></div>
    <span class="slide__dot" style="left:163px;"></span>
    <span class="slide__dot" style="left:323px;"></span>
    <h1 class="cover__title" style="margin:0;">Presentation Title -<br>Running in three or<br>more lines</h1>
    <div class="cover__brand">Harrowfield Engines</div>
  </section>

  <!-- Section screen -->
  <section class="slide slide--section" style="left:630px;top:390px;">
    <div class="slide__rule" style="top:187px;"></div>
    <span class="slide__dot" style="top:185px;left:265px;"></span>
    <h2 class="section__title" style="margin:0;">Section Title - long sentence in one line</h2>
    <div class="slide__brand" style="top:300px;">Harrowfield Engines</div>
  </section>

  <!-- Two graphs -->
  <section class="slide" style="left:100px;top:783px;">
    <div class="slide__rule"></div><span class="slide__dot" style="left:323px;"></span>
    <div class="slide__title">Section Title - long sentence in one line</div>
    <div class="slide__subtitle">Subsection title with 2 graphs</div>
    <div class="block" style="left:100px;top:114px;width:200px;">
      <div class="block__head">Lorem Ipsum Dolor Sit</div>
      <ol>
        <li>Lorem ipsum dolor sit amet, consectetuer adipiscing elit, sed diam nonummy nibh</li>
        <li>Lorem ipsum dolor sit amet, consectetuer adipiscing elit, sed diam nonummy</li>
        <li>Lnibh euismod tincidunt ut laoreet dolore magna Lnibh euismod tincidunt ut laoreet dolore magna.</li>
      </ol>
    </div>
    <div class="chart chart--purple" style="left:350px;top:62px;width:215px;height:132px;">
      <svg viewBox="0 0 211 128" role="img" aria-label="Bar chart of fund allocation by region">
        <text x="6" y="10" font-size="5" font-style="italic" fill="#666">Fund Allocation</text>
        <g font-size="3.5" fill="#666"><rect x="42" y="16" width="4" height="3" fill="#d6d6d6"/><text x="48" y="19">2019</text><rect x="62" y="16" width="4" height="3" fill="#5a5a5a"/><text x="68" y="19">2021</text><rect x="82" y="16" width="4" height="3" fill="#b3a8e0"/><text x="88" y="19">2022</text><line x1="104" y1="17.5" x2="110" y2="17.5" stroke="#8272c4"/><text x="112" y="19">Trendline for 2022 R² = 0.037</text></g>
        <g stroke="#eee" stroke-width=".5"><line x1="14" y1="28" x2="205" y2="28"/><line x1="14" y1="50" x2="205" y2="50"/><line x1="14" y1="72" x2="205" y2="72"/><line x1="14" y1="94" x2="205" y2="94"/></g>
        <line x1="14" y1="116" x2="205" y2="116" stroke="#999" stroke-width=".5"/>
        <g font-size="3.5" fill="#666"><text x="6" y="29">100</text><text x="8" y="51">75</text><text x="8" y="73">50</text><text x="8" y="95">25</text><text x="10" y="117">0</text></g>
        <g fill="#d6d6d6"><rect x="31" y="97" width="8" height="19"/><rect x="76" y="85" width="8" height="31"/><rect x="121" y="106" width="8" height="10"/><rect x="166" y="82" width="8" height="34"/></g>
        <g fill="#5a5a5a"><rect x="40" y="39" width="8" height="77"/><rect x="85" y="97" width="8" height="19"/><rect x="130" y="112" width="8" height="4"/><rect x="175" y="61" width="8" height="55"/></g>
        <g fill="#b3a8e0"><rect x="49" y="97" width="8" height="19"/><rect x="94" y="85" width="8" height="31"/><rect x="139" y="107" width="8" height="9"/><rect x="184" y="82" width="8" height="34"/></g>
        <line x1="20" y1="97" x2="200" y2="88" stroke="#8272c4" stroke-width=".8"/>
        <g font-size="3.5" fill="#888"><text x="37" y="122">Europe</text><text x="80" y="122">N America</text><text x="131" y="122">Asia</text><text x="172" y="122">S America</text></g>
      </svg>
    </div>
    <div class="chart chart--magenta" style="left:350px;top:199px;width:215px;height:132px;">
      <svg viewBox="0 0 211 128" role="img" aria-label="Bar chart of fund allocation by region">
        <text x="6" y="10" font-size="5" font-style="italic" fill="#666">Fund Allocation</text>
        <g font-size="3.5" fill="#666"><rect x="42" y="16" width="4" height="3" fill="#d6d6d6"/><text x="48" y="19">2019</text><rect x="62" y="16" width="4" height="3" fill="#5a5a5a"/><text x="68" y="19">2021</text><rect x="82" y="16" width="4" height="3" fill="#dba6c2"/><text x="88" y="19">2022</text><line x1="104" y1="17.5" x2="110" y2="17.5" stroke="#8272c4"/><text x="112" y="19">Trendline for 2022 R² = 0.037</text></g>
        <g stroke="#eee" stroke-width=".5"><line x1="14" y1="28" x2="205" y2="28"/><line x1="14" y1="50" x2="205" y2="50"/><line x1="14" y1="72" x2="205" y2="72"/><line x1="14" y1="94" x2="205" y2="94"/></g>
        <line x1="14" y1="116" x2="205" y2="116" stroke="#999" stroke-width=".5"/>
        <g font-size="3.5" fill="#666"><text x="6" y="29">100</text><text x="8" y="51">75</text><text x="8" y="73">50</text><text x="8" y="95">25</text><text x="10" y="117">0</text></g>
        <g fill="#d6d6d6"><rect x="31" y="97" width="8" height="19"/><rect x="76" y="85" width="8" height="31"/><rect x="121" y="106" width="8" height="10"/><rect x="166" y="82" width="8" height="34"/></g>
        <g fill="#5a5a5a"><rect x="40" y="39" width="8" height="77"/><rect x="85" y="97" width="8" height="19"/><rect x="130" y="84" width="8" height="32"/><rect x="175" y="61" width="8" height="55"/></g>
        <g fill="#dba6c2"><rect x="49" y="97" width="8" height="19"/><rect x="94" y="85" width="8" height="31"/><rect x="139" y="107" width="8" height="9"/><rect x="184" y="82" width="8" height="34"/></g>
        <line x1="20" y1="97" x2="200" y2="88" stroke="#8272c4" stroke-width=".8"/>
        <g font-size="3.5" fill="#888"><text x="37" y="122">Europe</text><text x="80" y="122">N America</text><text x="131" y="122">Asia</text><text x="172" y="122">S America</text></g>
      </svg>
    </div>
    <div class="slide__brand">Harrowfield Engines</div>
    <div class="slide__stamp">NOT FOR CIRCULATION</div>
  </section>

  <!-- Line graph with footnotes -->
  <section class="slide" style="left:748px;top:783px;">
    <div class="slide__rule"></div><span class="slide__dot" style="left:323px;"></span>
    <div class="slide__title">Section Title</div>
    <div class="slide__subtitle">Subsection title with a LINE graph and two footnotes</div>
    <div class="block" style="left:100px;top:114px;width:185px;">
      <div class="block__head">Lorem Ipsum Dolor Sit</div>
      <p>Lorem ipsum dolor sit amet, consectetuer adipiscing elit, sed diam nonummy nibh Lorem ipsum dolor sit amet*</p>
      <p style="margin-top:18px;">Lnibh euismod tincidunt ut laoreet dolore magna.**</p>
    </div>
    <div class="chart chart--line" style="left:315px;top:96px;width:288px;height:174px;">
      <svg viewBox="0 0 284 170" role="img" aria-label="Line chart of projection versus achievement over a decade">
        <text x="4" y="10" font-size="8" fill="#555">Decade that was  (in £M)</text>
        <g font-size="4.5" fill="#555"><circle cx="99" cy="30" r="2.2" fill="#bbb"/><text x="104" y="32">Projection</text><line x1="140" y1="30" x2="146" y2="30" stroke="#8272c4" stroke-width="1.4"/><text x="149" y="32">Achievement</text></g>
        <g font-size="4.5" fill="#555"><text x="5" y="28">60</text><text x="5" y="40">50</text><text x="5" y="55">40</text><text x="5" y="75">30</text><text x="5" y="103">20</text></g>
        <path d="M28 85 C38 60 45 50 52 70 C60 110 66 150 72 135 C80 110 95 45 108 55 C120 65 135 50 150 55 C165 60 175 55 190 58 C205 62 215 52 235 58 C250 62 258 50 266 48" fill="none" stroke="#aaa" stroke-width="1" stroke-dasharray="3 2"/>
        <path d="M30 75 C40 85 48 92 58 86 C70 80 85 68 100 66 C110 64 120 62 130 60 C140 55 150 58 165 56 C180 54 195 56 210 52 C225 49 245 42 268 22" fill="none" stroke="#8272c4" stroke-width="1.1"/>
        <g font-size="4.5" fill="#999"><text x="22" y="148">2010</text><text x="48" y="148">2011</text><text x="75" y="148">2012</text><text x="101" y="148">2013</text><text x="127" y="148">2014</text><text x="153" y="148">2015</text><text x="180" y="148">2016</text><text x="206" y="148">2017</text><text x="232" y="148">2018</text><text x="259" y="148">2019</text></g>
        <text x="122" y="162" font-size="4.8" fill="#555">Duration of analysis</text>
      </svg>
    </div>
    <div class="footnotes">* Lorem ipsum dolor sit amet, consectetuer adipiscing elit, sed diam nonummy nibh. Lorem ipsum dolor sit amet<br>**Lnibh euismod tincidunt ut laoreet dolore magna.</div>
    <div class="slide__brand">Harrowfield Engines</div>
    <div class="slide__stamp">NOT FOR CIRCULATION</div>
  </section>

  <!-- Table -->
  <section class="slide" style="left:426px;top:1171px;">
    <div class="slide__rule"></div><span class="slide__dot" style="left:323px;"></span>
    <div class="slide__title">Section Title - a different one and longer than ever in one line</div>
    <div class="slide__subtitle">Subsection title with table</div>
    <div class="block" style="left:100px;top:114px;width:160px;">
      <div class="block__head">Lorem Ipsum Dolor Sit</div>
      <ol>
        <li>Lorem ipsum dolor sit amet.</li>
        <li>Lorem ipsum dolor sit amet, consectetuer adipiscing elitsed.</li>
        <li>Lnibh euismod tincidunt ut laoreet dolore magna.</li>
      </ol>
    </div>
    <table class="datatable">
      <thead><tr><th>Purchase<br>_time</th><th>Sales_id</th><th>customer<br>_id</th><th>currency</th><th>Amount<br>_paid</th><th>device</th><th>Has<br>_discount</th><th>Agent<br>_comment</th></tr></thead>
      <tbody>
        <tr><td></td><td></td><td></td><td></td><td></td><td></td><td></td><td></td></tr>
        <tr><td></td><td></td><td></td><td></td><td></td><td></td><td></td><td></td></tr>
        <tr><td></td><td></td><td></td><td></td><td></td><td></td><td></td><td></td></tr>
        <tr><td></td><td></td><td></td><td></td><td></td><td></td><td></td><td></td></tr>
        <tr><td></td><td></td><td></td><td></td><td></td><td></td><td></td><td></td></tr>
        <tr><td></td><td></td><td></td><td></td><td></td><td></td><td></td><td></td></tr>
        <tr><td></td><td></td><td></td><td></td><td></td><td></td><td></td><td></td></tr>
        <tr><td></td><td></td><td></td><td></td><td></td><td></td><td></td><td></td></tr>
      </tbody>
    </table>
    <div class="slide__brand">Harrowfield Engines</div>
    <div class="slide__stamp">NOT FOR CIRCULATION</div>
  </section>

  <!-- Two-column text -->
  <section class="slide" style="left:100px;top:1588px;">
    <div class="slide__rule"></div><span class="slide__dot" style="left:323px;"></span>
    <div class="slide__title">Section Title - long sentence in one line</div>
    <div class="slide__subtitle">Subsection title</div>
    <div class="block" style="left:100px;top:114px;width:200px;">
      <div class="block__head">Lorem Ipsum Dolor Sit</div>
      <ol>
        <li>Lorem ipsum dolor sit amet, consectetuer adipiscing elit, sed diam nonummy nibh</li>
        <li>Lorem ipsum dolor sit amet, consectetuer adipiscing elit, sed diam nonummy</li>
        <li>Lnibh euismod tincidunt ut laoreet dolore magna Lnibh euismod tincidunt ut laoreet dolore magna.</li>
      </ol>
    </div>
    <div class="block" style="left:364px;top:114px;width:205px;">
      <div class="block__head">Lorem Ipsum</div>
      <ol>
        <li>Lorem ipsum dolor sit amet,</li>
        <li>Lorem ipsum dolor sit amet, consectetuer adipiscing elit, sed diam nonummy</li>
        <li>Lnibh euismod tincidunt ut laoreet dolore magna Lnibh euismod tincidunt ut laoreet dolore magna. dolore magna Lnibh euismod tincidunt ut laoreet dolore magna.</li>
        <li>Lorem ipsum dolor sit amet,</li>
        <li>Lorem ipsum dolor sit amet, consectetuer adipiscing elit, sed diam nonummy</li>
      </ol>
    </div>
    <div class="slide__brand">Harrowfield Engines</div>
    <div class="slide__stamp">NOT FOR CIRCULATION</div>
  </section>

  <!-- Wide text -->
  <section class="slide" style="left:748px;top:1588px;">
    <div class="slide__rule"></div><span class="slide__dot" style="left:323px;"></span>
    <div class="slide__title">Section Title - long sentence in one line</div>
    <div class="slide__subtitle">Subsection title with 1 wide text</div>
    <div class="banded">
      <div class="block__head">Lorem Ipsum Dolor Sit</div>
      <ol>
        <li><span>1.</span><span>Lorem ipsum dolor sit amet,</span></li>
        <li><span>2.</span><span>Lorem ipsum dolor sit amet, consectetuer adipiscing elit, sed diam nonummy</span></li>
        <li><span>3.</span><span>Lnibh euismod tincidunt ut laoreet dolore magna Lnibh euismod tincidunt ut laoreet dolore magna. dolore magna Lnibh euismod tincidunt ut laoreet dolore magna.</span></li>
        <li><span>4.</span><span>Lorem ipsum dolor sit amet,</span></li>
        <li><span>5.</span><span>Lorem ipsum dolor sit amet, consectetuer adipiscing elit, sed diam nonummy</span></li>
      </ol>
    </div>
    <div class="slide__brand">Harrowfield Engines</div>
    <div class="slide__stamp">NOT FOR CIRCULATION</div>
  </section>

  <!-- Disclaimer -->
  <section class="slide" style="left:100px;top:1960px;">
    <div class="slide__rule"></div><span class="slide__dot" style="left:323px;"></span>
    <div class="slide__title">Disclaimer</div>
    <div class="legal" style="left:26px;">
      <p>Lorem ipsum dolor sit amet, consectetuer adip iscing elit, sed diam nonummy nibh Lorem ipsum dolor sit amet Lorem ipsum dolor sit amet, consectetuer adip iscing elit, sed diam nonummy nibh Lorem ipsum dolor sit amet. Lnibh euismod tincidunt ut laoreet dolore magna. Lorem ipsum dolor sit amet, consectetuer adip iscing elit, sed diam nonummy nibh Lorem ipsum dolor sit amet. Lorem ipsum dolor sit amet, consectetuer adip iscing elit, sed diam nonummy nibh Lorem ipsum dolor sit amet Lorem ipsum dolor sit amet, consectetuer adip iscing elit, sed diam nonummy nibh Lorem ipsum dolor sit amet. Lorem ipsum dolor sit amet, consectetuer adip iscing elit, sed diam nonummy nibh Lorem ipsum dolor sit amet Lorem ipsum dolor sit amet, consectetuer adip iscing elit, sed diam nonummy nibh Lorem ipsum dolor sit amet. Lorem ipsum dolor sit amet, consectetuer adip iscing elit, sed diam nonummy nibh Lorem ipsum dolor sit amet.</p>
      <p>Lorem ipsum dolor sit amet, consectetuer adip iscing elit, sed diam nonummy nibh Lorem ipsum dolor sit amet Lorem ipsum dolor sit amet, consectetuer adip iscing elit, sed diam nonummy nibh Lorem ipsum dolor sit amet. Lorem ipsum dolor sit amet, consectetuer adip iscing elit, sed diam nonummy nibh Lorem ipsum dolor sit amet Lorem ipsum dolor sit amet, consectetuer adip iscing elit, sed diam nonummy nibh Lorem ipsum dolor sit amet.</p>
    </div>
    <div class="legal" style="left:322px;">
      <p>Dolor sit amet, consectetuer adip iscing elit, sed diam nonummy nibh Lorem ipsum dolor sit amet Lorem ipsum dolor sit amet, consectetuer adip iscing elit, sed diam nonummy nibh Lorem ipsum dolor sit amet. Lnibh euismod tincidunt ut laoreet dolore magna. Lorem ipsum dolor sit amet, consectetuer adip iscing elit, sed diam nonummy nibh Lorem ipsum dolor sit amet. Sit amet, consectetuer adip iscing elit, sed diam nonummy nibh Lorem ipsum dolor sit amet Lorem ipsum dolor sit amet, consectetuer adip iscing elit, sed diam nonummy nibh Lorem ipsum dolor sit amet. Lorem ipsum dolor sit amet, consectetuer adip iscing elit, sed diam nonummy nibh Lorem ipsum dolor sit amet. Lorem ipsum dolor sit amet, consectetuer adip iscing elit, sed diam nonummy nibh Lorem ipsum dolor sit amet, consectetuer adip iscing elit, sed diam nonummy nibh.</p>
      <p>Lorem ipsum dolor sit amet. Lorem ipsum dolor sit amet, consectetuer adip iscing elit, sed diam nonummy nibh. Lorem ipsum dolor sit amet Lorem ipsum dolor sit amet, consectetuer adip iscing elit, sed diam nonummy nibh Lorem ipsum dolor sit amet. Lorem ipsum dolor sit amet, consectetuer adip iscing elit, sed diam nonummy. Lorem ipsum dolor sit amet Lorem ipsum dolor sit amet, consectetuer adip iscing elit, sed diam nonummy nibh.</p>
    </div>
    <div class="slide__brand">Harrowfield Engines</div>
    <div class="slide__stamp">NOT FOR CIRCULATION</div>
  </section>

  <!-- Biographies -->
  <section class="slide" style="left:748px;top:1960px;">
    <div class="slide__rule"></div><span class="slide__dot" style="left:323px;"></span>
    <div class="slide__title">Heading for Biographies</div>
    <article class="bio" style="left:83px;">
      <h3>Lorem Ipsum, Dolor, SIT</h3>
      <p>Lorem ipsum dolor sit amet, consectetuer adip iscing elit, sed diam nonummy nibh Lorem ipsum dolor sit amet Lorem ipsum dolor sit amet, consectetuer adip iscing elit, sed diam nonummy nibh Lorem ipsum dolor sit amet.<br>Lnibh euismod tincidunt ut laoreet dolore magna. Lorem ipsum dolor sit amet, consectetuer adip iscing elit, sed diam nonummy nibh Lorem ipsum dolor sit amet.<br>Lorem ipsum dolor sit amet, consectetuer adip iscing elit, sed diam nonummy nibh Lorem ipsum dolor sit amet.</p>
    </article>
    <article class="bio" style="left:347px;">
      <h3>Lorem Ipsum, Dolor sit</h3>
      <p>Lorem ipsum dolor sit amet, consectetuer adip iscing elit, sed diam nonummy nibh Lorem ipsum dolor sit amet Lorem ipsum dolor sit amet, consectetuer adip iscing elit, sed diam nonummy nibh Lorem ipsum dolor sit amet.<br>Lnibh euismod tincidunt ut laoreet dolore magna. Lorem ipsum dolor sit amet, consectetuer adip iscing elit, sed diam nonummy nibh Lorem ipsum dolor sit amet.<br>Lorem ipsum dolor sit amet, consectetuer adip iscing elit, sed diam nonummy nibh Lorem ipsum dolor sit amet.</p>
    </article>
    <div class="slide__brand">Harrowfield Engines</div>
    <div class="slide__stamp">NOT FOR CIRCULATION</div>
  </section>

</div>
</div>
</body>
</html>
```